I need to launch a new website that more accurately reflects what we do as a business. We are an IT Reseller that specialises in delivering innovative solutions covering supply, implementation and support. My current website is www.vornetikx.com and was something I designed myself on the Hub Nimbo website. This was fine for the first 2 years but now I need something more professional and detailed. A couple of websites for companies similar to Brindle KTR are www.quarvolen.co.uk and www.ferrimund.co.uk. By looking at these it will hopefully give you an idea as to what I am trying to achieve.

Target Market(s)

UK based companies with between 30-250 employees, no fixed vertical

Coding

Coded - Design and coding required

Number of Pages Required

4 page

Font styles to use
Sans Serif

Colors
33a6d7
0592cd
85cae6

Requirements
Must have
• Contact details page to include a "Get in touch with us " section, About Us page, IT Support page to include the headings 1/ Proactive Monitoring 2/ 24 x 7 Support 3/ Security and Data Back-up 4/ Built-in Compliance (GDPR) 5/ Responsive IT Support. I am happy to provide the wording for these headings.
Clean crisp home screen with a Menu offering the requested drop down options.
Nice to have
• Easy to navigate site with a good flow. I have updated a page regarding cloud services, this would be great to have as a separate drop down menu option. I would like to have different Cloud logo's in ideally the Brindle Blue colour. Can you please add the photograph of Thornwick Lodge which is my office in the contact us page.
Should not have
• I definitely DO NOT want a photo/view of London on the home page!!

```html
<!DOCTYPE html>
<html lang="en">
<head>
<meta charset="utf-8">
<title>Brindle KTR – Experienced, Personalised IT Consulting</title>
<link href="https://fonts.googleapis.com/css2?family=Open+Sans:wght@400;600;700;800&display=swap" rel="stylesheet">
<style>
:root{
  --blue:#0592cd;
  --blue-bright:#33a6d7;
  --blue-soft:#85cae6;
  --ink:#2b2b33;
  --text:#7a7a85;
  --page-tint:#f4f6fc;
  --white:#ffffff;
  --footer:#2a2a2e;
  --footer-bottom:#1f1f22;
  --footer-text:#d6d6da;
}
*{box-sizing:border-box;margin:0;padding:0}
html,body{width:1200px;height:3848px;overflow:hidden}
body{font-family:"Open Sans",Arial,sans-serif;color:var(--ink);background:var(--white);position:relative}
.abs{position:absolute}

/* header + hero */
.hero{position:absolute;left:0;top:0;width:1200px;height:583px;
  background:radial-gradient(ellipse at 55% 70%,#2a5f9a 0%,#123763 35%,#0a1a33 70%,#050b17 100%);}
.hero-shade{position:absolute;inset:0;background:linear-gradient(180deg,rgba(0,0,0,.55) 0%,rgba(0,0,0,.1) 30%,rgba(0,0,0,.15) 100%)}
.brand{position:absolute;display:flex;align-items:center;gap:12px;color:var(--white);font-size:22px;font-weight:400}
.brand-mark{width:44px;height:44px;background:var(--blue);border-radius:4px}
.nav{position:absolute;top:58px;left:436px;display:flex;gap:0;font-size:12px;font-weight:700;color:var(--white);letter-spacing:.2px}
.nav a{color:inherit;text-decoration:none;position:absolute;white-space:nowrap}
.nav a.active{color:var(--blue-bright)}
.btn{display:flex;align-items:center;justify-content:center;border-radius:22px;font-size:12px;font-weight:700;letter-spacing:.4px;text-decoration:none}
.btn-solid{background:var(--blue);color:var(--white)}
.btn-ghost-light{border:1.5px solid rgba(255,255,255,.85);color:var(--white)}
.btn-ghost{border:1.5px solid #b8b8c0;color:#55555f;background:var(--white)}
.hero-title{position:absolute;left:0;width:1200px;top:232px;text-align:center;color:var(--white);font-size:54px;font-weight:700;line-height:62px;letter-spacing:.5px}

/* partner strip */
.partners{position:absolute;left:0;top:583px;width:1200px;height:94px;background:var(--white)}
.partner{position:absolute;top:34px;font-size:19px;font-weight:600;color:#55555f;transform:translateX(-50%);white-space:nowrap}

/* what we do */
.services{position:absolute;left:0;top:677px;width:1200px;height:989px;background:var(--page-tint);overflow:hidden}
.section-title{position:absolute;left:0;width:1200px;text-align:center;font-size:32px;font-weight:700;color:var(--ink)}
.section-title em{font-style:normal;color:var(--blue)}
.card{position:absolute;width:331px;height:343px;background:var(--white);box-shadow:0 2px 14px rgba(40,60,120,.06);text-align:center}
.card-icon{position:absolute;left:50%;top:34px;transform:translateX(-50%)}
.card-title{position:absolute;left:0;width:100%;top:102px;font-size:17px;font-weight:700;letter-spacing:.3px;color:var(--ink)}
.card-text{position:absolute;left:30px;right:24px;top:138px;font-size:13px;line-height:21px;color:var(--text);text-align:justify}
.card .btn{position:absolute;left:50%;top:268px;width:149px;height:41px;transform:translateX(-50%)}

/* banner */
.banner{position:absolute;left:0;top:1666px;width:1200px;height:423px;
  background:linear-gradient(100deg,#3a3d44 0%,#6b6e75 35%,#9a9ca1 65%,#7d8087 100%)}
.banner-shade{position:absolute;inset:0;background:rgba(40,42,48,.45)}
.banner-title{position:absolute;left:0;width:1200px;top:90px;text-align:center;color:var(--white);font-size:44px;font-weight:700;line-height:51px}
.banner-sub{position:absolute;left:0;width:1200px;top:211px;text-align:center;color:var(--white);font-size:21px;line-height:32px}

/* advantages */
.advantages{position:absolute;left:0;top:2089px;width:1200px;height:623px;background:var(--page-tint)}
.adv-card{position:absolute;top:170px;width:331px;height:342px;background:var(--white);box-shadow:0 2px 14px rgba(40,60,120,.06)}
.adv-illus{position:absolute;left:50%;top:30px;width:92px;height:92px;border-radius:50%;transform:translateX(-50%)}
.adv-title{position:absolute;left:0;width:100%;top:134px;text-align:center;font-size:17px;font-weight:700;color:var(--blue)}
.adv-text{position:absolute;left:27px;right:25px;top:168px;font-size:13px;line-height:21px;color:var(--text);text-align:justify}

/* testimonial */
.testimonial{position:absolute;left:0;top:2712px;width:1200px;height:624px;background:var(--white)}
.quote-badge{position:absolute;left:55px;top:279px;width:90px;height:90px;border-radius:50%;background:var(--blue);color:var(--white);font-size:44px;font-weight:800;display:flex;align-items:center;justify-content:center;box-shadow:0 0 0 18px #eef0f3}
.t-heading{position:absolute;left:626px;top:150px;font-size:35px;font-weight:700;line-height:39px;color:var(--ink)}
.t-text{position:absolute;left:626px;top:278px;width:480px;font-size:14px;line-height:26.5px;color:var(--text)}
.t-name{position:absolute;left:626px;top:400px;font-size:14px;color:var(--blue)}

/* footer */
.footer{position:absolute;left:0;top:3336px;width:1200px;height:426px;background:var(--footer);color:var(--footer-text)}
.footer-address{position:absolute;left:73px;top:168px;font-size:14px;line-height:26.5px}
.footer-mail{position:absolute;left:73px;top:272px;font-size:14px;line-height:26.5px;color:var(--blue-bright)}
.footer-heading{position:absolute;top:80px;font-size:22px;color:var(--white)}
.footer-list{position:absolute;list-style:none;font-size:14px;line-height:35px;color:var(--footer-text)}
.social{position:absolute;top:218px;display:flex;gap:22px;left:986px}
.social span{width:18px;height:18px;border-radius:50%;background:#8a8a92}
.social span:first-child{background:var(--blue-bright)}
.copyright{position:absolute;left:0;top:3762px;width:1200px;height:86px;background:var(--footer-bottom);color:#b8b8bd;font-size:13px;text-align:center;line-height:86px}
</style>
</head>
<body>

<header class="hero">
  <div class="abs" role="img" aria-label="Photograph of a data centre corridor lined with glowing server racks" style="inset:0"></div>
  <div class="hero-shade"></div>
  <div class="brand" style="left:73px;top:41px"><span class="brand-mark"></span>Brindle KTR</div>
  <nav class="nav">
    <a class="active" style="left:0">HOME</a>
    <a style="left:94px">ABOUT US</a>
    <a style="left:213px">SERVICES</a>
    <a style="left:325px">BLOG</a>
    <a style="left:414px">CONTACT US</a>
  </nav>
  <a class="btn btn-solid abs" style="left:976px;top:43px;width:149px;height:42px">GET IN TOUCH</a>
  <h1 class="hero-title">EXPERIENCED, PERSONALISED<br>IT CONSULTING</h1>
  <a class="btn btn-ghost-light abs" style="left:509px;top:395px;width:148px;height:40px">READ MORE</a>
</header>

<section class="partners" aria-label="Partners">
  <span class="partner" style="left:178px">Corvane Partners</span>
  <span class="partner" style="left:395px">Tablix</span>
  <span class="partner" style="left:593px">Roundclock</span>
  <span class="partner" style="left:805px">Crateloom</span>
  <span class="partner" style="left:1038px">Skyvault Hosting</span>
</section>

<section class="services">
  <svg class="abs" style="left:0;top:0" width="1200" height="989" aria-hidden="true">
    <polygon points="1200,60 1200,220 560,520" fill="#e9edfa"/>
    <polygon points="0,820 520,560 0,989" fill="#e9edfa"/>
  </svg>
  <h2 class="section-title" style="top:68px">WHAT <em>WE DO</em></h2>

  <article class="card" style="left:73px;top:169px">
    <svg class="card-icon" width="54" height="56" viewBox="0 0 54 56" fill="none" stroke="#0592cd" stroke-width="2"><rect x="4" y="4" width="46" height="34" rx="2"/><circle cx="27" cy="24" r="9"/><line x1="33" y1="31" x2="40" y2="38"/><line x1="27" y1="38" x2="27" y2="50"/><circle cx="27" cy="52" r="2.5"/></svg>
    <h3 class="card-title">PROACTIVE MONITORING</h3>
    <p class="card-text">Whether it is a fully managed service agreement, remote managed service or simply advice on where you are and where you could get to we have the knowledge and skills to assist you.</p>
    <a class="btn btn-ghost">READ MORE</a>
  </article>
  <article class="card" style="left:433px;top:169px">
    <svg class="card-icon" width="56" height="56" viewBox="0 0 56 56" fill="none" stroke="#0592cd" stroke-width="2"><circle cx="32" cy="24" r="20"/><polyline points="32,12 32,24 40,28"/><circle cx="16" cy="38" r="8"/><path d="M6 54c0-7 4-10 10-10s10 3 10 10"/></svg>
    <h3 class="card-title">24/7 SERVER MONITORING</h3>
    <p class="card-text">Whether it is a fully managed service agreement, remote managed service or simply advice on where you are and where you could get to we have the knowledge and skills to assist you.</p>
    <a class="btn btn-ghost">READ MORE</a>
  </article>
  <article class="card" style="left:793px;top:169px">
    <svg class="card-icon" width="44" height="56" viewBox="0 0 44 56" fill="none" stroke="#0592cd" stroke-width="2"><circle cx="22" cy="14" r="10"/><circle cx="22" cy="14" r="4"/><rect x="10" y="28" width="24" height="14" rx="2"/><line x1="14" y1="42" x2="14" y2="54"/><line x1="30" y1="42" x2="30" y2="54"/><line x1="22" y1="42" x2="22" y2="54"/></svg>
    <h3 class="card-title">DEDICATED IT TEAM</h3>
    <p class="card-text">Whether it is a fully managed service agreement, remote managed service or simply advice on where you are and where you could get to we have the knowledge and skills to assist you.</p>
    <a class="btn btn-ghost">READ MORE</a>
  </article>

  <article class="card" style="left:73px;top:548px">
    <svg class="card-icon" width="54" height="54" viewBox="0 0 54 54" fill="none" stroke="#0592cd" stroke-width="2"><circle cx="27" cy="27" r="23"/><circle cx="27" cy="27" r="14"/><circle cx="27" cy="27" r="6"/><line x1="27" y1="4" x2="27" y2="13"/><line x1="27" y1="41" x2="27" y2="50"/><line x1="4" y1="27" x2="13" y2="27"/><line x1="41" y1="27" x2="50" y2="27"/></svg>
    <h3 class="card-title">DEVOPS SERVICES</h3>
    <p class="card-text">Whether it is a fully managed service agreement, remote managed service or simply advice on where you are and where you could get to we have the knowledge and skills to assist you.</p>
    <a class="btn btn-ghost">READ MORE</a>
  </article>
  <article class="card" style="left:433px;top:548px">
    <svg class="card-icon" width="56" height="54" viewBox="0 0 56 54" fill="none" stroke="#0592cd" stroke-width="2"><path d="M16 22a9 9 0 0 1 2-17 12 12 0 0 1 22 4 8 8 0 0 1 0 13z"/><rect x="4" y="30" width="14" height="20"/><rect x="22" y="30" width="14" height="20"/><rect x="40" y="36" width="12" height="14"/><line x1="28" y1="22" x2="28" y2="30"/></svg>
    <h3 class="card-title">IT MANAGED SERVICE</h3>
    <p class="card-text">Whether it is a fully managed service agreement, remote managed service or simply advice on where you are and where you could get to we have the knowledge and skills to assist you.</p>
    <a class="btn btn-ghost">READ MORE</a>
  </article>
  <article class="card" style="left:793px;top:548px">
    <svg class="card-icon" width="54" height="54" viewBox="0 0 54 54" fill="none" stroke="#0592cd" stroke-width="2"><rect x="16" y="4" width="24" height="30" rx="2"/><line x1="21" y1="12" x2="35" y2="12"/><line x1="21" y1="19" x2="35" y2="19"/><path d="M4 38h14l6 6h26v6H4z"/></svg>
    <h3 class="card-title">PROCUREMENT</h3>
    <p class="card-text">Whether it is a fully managed service agreement, remote managed service or simply advice on where you are and where you could get to we have the knowledge and skills to assist you.</p>
    <a class="btn btn-ghost">READ MORE</a>
  </article>
</section>

<section class="banner">
  <div class="abs" role="img" aria-label="Photograph of a modern office desk with a desktop computer and framed print" style="inset:0"></div>
  <div class="banner-shade"></div>
  <h2 class="banner-title">A NEW AND PERSONALISED<br>LEVEL OF SERVICE</h2>
  <p class="banner-sub">Find out what it is like to have a customised service tailored to your<br>business requirements today and for the future.</p>
  <a class="btn btn-solid abs" style="left:525px;top:304px;width:150px;height:40px">GET IN TOUCH</a>
</section>

<section class="advantages">
  <h2 class="section-title" style="top:52px">BRINDLE KTR <em>ADVANTAGES</em></h2>
  <article class="adv-card" style="left:73px">
    <div class="adv-illus" role="img" aria-label="Illustration of a blue cloud" style="background:linear-gradient(180deg,#eef2f8,#cfe6f5)"></div>
    <h3 class="adv-title">OUR EXPERIENCE</h3>
    <p class="adv-text">With a wealth of knowledge within the IT Service delivery industry we are confident that we can become the trusted adviser and partner to you and your business. With a personal and tailored solution that will grow and develop along with your business.</p>
  </article>
  <article class="adv-card" style="left:434px">
    <div class="adv-illus" role="img" aria-label="Illustration of a consultant in a suit" style="background:linear-gradient(180deg,#eef2f8,#c9d8ec)"></div>
    <h3 class="adv-title">OUR APPROACH</h3>
    <p class="adv-text">With a wealth of knowledge within the IT Service delivery industry we are confident that we can become the trusted adviser and partner to you and your business. With a personal and tailored solution that will grow and develop along with your business.</p>
  </article>
  <article class="adv-card" style="left:795px">
    <div class="adv-illus" role="img" aria-label="Illustration of an office building" style="background:linear-gradient(180deg,#eef2f8,#cddcf0)"></div>
    <h3 class="adv-title">WHY US?</h3>
    <p class="adv-text">With a wealth of knowledge within the IT Service delivery industry we are confident that we can become the trusted adviser and partner to you and your business. With a personal and tailored solution that will grow and develop along with your business.</p>
  </article>
</section>

<section class="testimonial">
  <svg class="abs" style="left:95px;top:80px" width="480" height="480" viewBox="0 0 480 480">
    <path d="M70 30 C170 -10 360 10 440 90 C500 160 470 300 380 380 C300 450 170 470 90 440 C20 410 -10 330 10 240 C25 160 10 60 70 30Z" fill="#eef8f4"/>
    <path d="M60 60 C150 20 320 40 400 120 C460 190 430 320 340 390 C260 450 150 450 80 420 C10 390 0 300 10 220 C20 150 0 90 60 60Z" fill="url(#techGlow)" role="img" aria-label="Illustration of a hand holding glowing network technology icons"/>
    <defs><radialGradient id="techGlow" cx="55%" cy="45%" r="65%"><stop offset="0" stop-color="#9fd6f2"/><stop offset=".45" stop-color="#2f7fc4"/><stop offset="1" stop-color="#0b1b3a"/></radialGradient></defs>
  </svg>
  <div class="quote-badge">&ldquo;</div>
  <h2 class="t-heading">What Our Clients are<br>Saying</h2>
  <p class="t-text">This is due to their excellent service, competitive pricing and customer support. It’s throughly refresing to get such a personal touch. Duis aute irure dolor in reprehenderit in voluptate velit esse cillum dolore eu fugiat nulla pariatur.</p>
  <p class="t-name">Marla Quenby</p>
  <svg class="abs" style="left:1060px;top:3251px;transform:translateY(-2712px)" width="66" height="18" viewBox="0 0 66 18" fill="none" stroke-width="2"><path d="M28 9H2M9 2 2 9l7 7" stroke="#0592cd"/><path d="M38 9h26M57 2l7 7-7 7" stroke="#b8b8c0"/></svg>
</section>

<footer class="footer">
  <div class="brand" style="left:73px;top:74px"><span class="brand-mark"></span>Brindle KTR</div>
  <p class="footer-address">Thornwick Lodge, Ashcombe Vale, Elmbury,<br>Fernshire, EB2 4QT,<br>United Kingdom</p>
  <p class="footer-mail">owen.tarrant@brindlektr.com<br>priya.halvorsen@brindlektr.com</p>
  <h3 class="footer-heading" style="left:467px">Quick Links</h3>
  <ul class="footer-list" style="left:470px;top:146px"><li>Home</li><li>About us</li><li>Services</li><li>Blog</li><li>Contact us</li></ul>
  <h3 class="footer-heading" style="left:705px">Our Services</h3>
  <ul class="footer-list" style="left:708px;top:150px"><li>Proactive monitoring</li><li>I24X7 Monitoring</li><li>Dedicated IT Support</li><li>Devops Team</li><li>IT managed services</li><li>Procurement</li></ul>
  <div class="social" aria-label="Social links"><span></span><span></span><span></span><span></span></div>
</footer>
<div class="copyright">Copyright © 2019 Brindle KTR - All Rights Reserved.</div>

</body>
</html>
```